Information flyer for 5 day treatment flyer

I am wanting a double sided flyer for my next 5 day treatment program for addictions. I have included the copy for the flyer as an attachment.
I have also included a drop box link to my brand guidelines and my logos. The logo I prefer is the grey horse with the words Willowmere Collective under.
https://www.filecrate.example/sh/k2jtq7wn3xb5lp1/BBQr9TzLm4Kd7c8NpWvY2hsXe?dl=0

https://www.filecrate.example/s/qm8vz2kt6bw9rc4/WILLOWMERE%20COLLECTIVE%20%7C%20Brand%20Identity%20Guidelines.pdf?dl=0
I have also included a copy of an existing flyer which I like very much and a documant with the copy.
https://www.filecrate.example/sh/t7wbn3kx9zq1mv5/CCRt2pLw8-nZ4Kj7FyTuGHs_b?dl=0

I prefer simple, elegant designs please. The design needs to show my clients that I know what I am doing and I am trust worthy and a skilled professional.

Here is the drop box link to the images I have selected for this program. The tones in the images I have selected are orange/red. Please feel free to pick what you think works well.
https://www.filecrate.example/sh/mrq5jv82lnc0tfw/DDDhW392Bx6Lp88_Q7KcZnRye?dl=0

Many thanks
Marisol

```html
<!DOCTYPE html>
<html lang="en">
<head>
<meta charset="utf-8">
<title>Willowmere Collective – 12 Day Intensive Program</title>
<link href="https://fonts.googleapis.com/css2?family=Questrial&family=Comfortaa:wght@300;400&display=swap" rel="stylesheet">
<style>
  :root{
    --ink:#1f2a3a;
    --body:#6a6f79;
    --paper:#fbfbfd;
    --mist:#dfe2ea;
    --frost:#c9cdd8;
    --rule:#2b2f36;
  }
  html,body{margin:0;padding:0;overflow:hidden;}
  body{width:848px;height:1200px;background:var(--paper);}
  .flyer{position:relative;width:848px;height:1200px;overflow:hidden;font-family:"Comfortaa",sans-serif;font-weight:300;color:var(--body);}
  .backdrop{position:absolute;inset:0;background:
      radial-gradient(ellipse 90% 35% at 45% 88%, rgba(170,176,192,.55), rgba(255,255,255,0) 70%),
      linear-gradient(180deg,#fdfdfe 0%,#f5f6f9 35%,#eceef3 60%,#dfe2ea 80%,#e8eaf0 100%);}
  .col{position:absolute;width:377px;}
  .col-left{left:46px;}
  .col-right{left:447px;}
  .block{position:absolute;left:0;width:100%;}
  h2{font-family:"Questrial",sans-serif;font-weight:400;color:var(--ink);font-size:20.5px;line-height:27px;margin:0;letter-spacing:.2px;}
  h3{font-family:"Questrial",sans-serif;font-weight:400;color:var(--ink);font-size:18px;line-height:22px;margin:0;}
  p{margin:0;font-size:12.2px;line-height:17.1px;}
  .justify p{text-align:justify;}
  ul.outcomes{list-style:none;margin:2px 0 0;padding:0;}
  ul.outcomes li{position:relative;padding-left:23px;font-size:12.2px;line-height:17.1px;margin-bottom:5.8px;}
  ul.outcomes li::before{content:"";position:absolute;left:6px;top:4px;width:8px;height:8px;background:#3a3d44;}
  .lines div{font-size:12.2px;line-height:17.1px;}
  .terms p{font-size:9.6px;line-height:13.7px;text-align:justify;}
  .footer{position:absolute;left:30px;top:1050px;width:400px;height:106px;}
  .brand{position:absolute;left:0;top:20px;width:150px;text-align:center;}
  .brand .dot{display:block;margin:0 auto 12px;width:40px;height:40px;border-radius:50%;background:#2a2d33;}
  .brand .name{font-family:"Questrial",sans-serif;font-size:11.5px;letter-spacing:2.4px;color:#2a2d33;line-height:15px;}
  .divider{position:absolute;left:149px;top:0;width:1px;height:106px;background:var(--rule);}
  .contact{position:absolute;left:165px;top:12px;font-size:10.4px;line-height:19.6px;color:#3a3d44;font-weight:400;}
  .contact div{display:flex;align-items:center;gap:7px;}
  .contact svg{width:9px;height:9px;flex:none;}
  .contact .abn{padding-left:16px;}
</style>
</head>
<body>
<div class="flyer">
  <div class="backdrop" role="img" aria-label="Soft faded photograph of a frosty, snow-covered landscape in pale grey-blue tones"></div>

  <div class="col col-left justify">
    <section class="block" style="top:38px">
      <h2>What Is Intimacy?</h2>
      <p>Intimacy is our emotional food - it sustains and nourishes us, helping us feel connected, understood and valued. Lack of emotional intimacy in our most important relationships creates problems such as anxiety, jealously, withdrawal, betrayal, abandonment and even infidelity.</p>
    </section>
    <section class="block" style="top:183px">
      <h2>Hunger Versus Love.</h2>
      <p>Emotional hunger is not love. This hunger is a strong need caused by emotional deprivation in childhood. Feelings of emotional hunger are experienced as deep internal sensations that range in intensity from a dull ache to a sharp painful feeling. Because of its intensity, this sensation is often confused with real love. Many people claim to be loving and caring, when in fact they are actually feeling their emotional hunger and neediness. Emotional hunger is what we experience when feeling abandonment pain. This keeps us in unfulfilling, destructive and addictive relationships.</p>
    </section>
    <section class="block" style="top:415px">
      <h2>This Program Focuses On Abandonment And Engulfment Issues.</h2>
      <p>To avoid the pain of abandonment and the overwhelming feelings of engulfment, in childhood we subconsciously learn to create a fantasy bond. Later this bond is transferred to our adult relationships, especially romantic and sexual ones. The fantasy bond is a primary defense against intimacy. According to Dr. Harold Penwarden, “the fantasy bond is a substitute for love and care that was missing in the child’s world. Many parents offer affection and love when they feel the need for it themselves. This type of physical affection drains the emotional resources of children rather than nourishing them. It is a form of taking, not giving.</p>
    </section>
    <section class="block" style="top:737px">
      <h2>Why Is It Important To Examine Our Childhood When Trying To Sort Out Our Issues In Adult Relationships Today?</h2>
      <p>Children are needy by nature, not by choice. They instinctively adapt their behaviour and personalities in order to get their emotional needs met. As a result of the fantasy bond, created between child and caregiver, we carry with us into adulthood the same survival mechanisms leading to a sacrifice of our freedom and any real intimacy in loving relationships. Instead, we create dependencies with people, substances and behaviour patterns to fill the deep emptiness or loneliness within us.</p>
    </section>
  </div>

  <div class="col col-right">
    <section class="block" style="top:38px">
      <h2>During This 12 Day Intensive Program You Will:</h2>
      <ul class="outcomes">
        <li>Identify what you need to do for yourself to stop destructive relationship patterns.</li>
        <li>Learn how to protect yourself from feeling over whelmed or drained in close relationships.</li>
        <li>Release emotional baggage from past adult relationships.</li>
        <li>Significantly heal childhood abandonment and engulfment issues.</li>
        <li>Identify the subconscious negative beliefs that are sabotaging you from having the relationship you desire.</li>
        <li>Release childhood trauma out of your body from abuse and neglect</li>
        <li>Learn how to set healthy boundaries - physically, emotionally, spiritually, intellectually and sexually.</li>
        <li>Differentiate between needs and values - the drivers in relationships.</li>
        <li>Identify your needs and values and determine steps to take to meet them.</li>
        <li>Free yourself of shame, guilt and fear from child hood and adult relationships.</li>
        <li>Communicate your needs and ask for what you want without feeling too embarrassed or vulnerable.</li>
        <li>Create healthy self-esteem and love - the foundation for intimacy.</li>
      </ul>
    </section>
    <section class="block lines" style="top:610px">
      <h2>Program Details&nbsp; (When)</h2>
      <div>Thursday 25th October 6:00pm - 9:00pm</div>
      <div>Friday, 26th October 9:00pm - 5:00pm</div>
      <div>Saturday, 27th October 9:00pm - 9:00pm</div>
      <div>Sunday, 28th October 9:00pm - 5:00pm</div>
      <div>Monday, 29th October 9:00pm - 4:00pm</div>
    </section>
    <section class="block justify" style="top:734px">
      <h2>Enrolment Process</h2>
      <p>This 5 day program is limited in numbers and offers individual and group time. Enrolments close Friday, 19th October 2018. To book your place, register your interest or find out more about this program please call Marisol 0400 555 219. Out of town participants please contact our office for assistance with accommodation if required.</p>
    </section>
    <section class="block lines" style="top:889px">
      <h2>Inclusions</h2>
      <div>A pre-assessment phone consult</div>
      <div>Relevant on online diagnostic survey’s</div>
      <div>Integrated Equine Assisted Psychotherapy</div>
      <div>Ropes course</div>
      <div>All course materials (notebook, writing materials),</div>
      <div>Morning and afternoon tea daily,</div>
    </section>
    <section class="block lines" style="top:1027px">
      <h2>Investments :</h2>
      <div>$2250 including GST</div>
    </section>
    <section class="block terms" style="top:1088px">
      <h3>Terms &amp; Conditions</h3>
      <p>A non-refundable deposit of $500 is required to hold your place. Enrolments with full payment is required by Tuesday, 23th October 2018. Charge card transactions incur a 3.3% merchant fee, other credit cards 2.5%. EFTPOS facility available.</p>
    </section>
  </div>

  <footer class="footer">
    <div class="brand">
      <span class="dot"></span>
      <div class="name">WILLOWMERE<br>COLLECTIVE</div>
    </div>
    <div class="divider"></div>
    <div class="contact">
      <div class="abn">ABN 12 345 678 901</div>
      <div><svg viewBox="0 0 10 10"><path d="M5 .5a3.2 3.2 0 0 0-3.2 3.2C1.8 6.2 5 9.5 5 9.5s3.2-3.3 3.2-5.8A3.2 3.2 0 0 0 5 .5z" fill="none" stroke="#3a3d44"/><circle cx="5" cy="3.7" r="1.1" fill="#3a3d44"/></svg>27 Fernhollow Road, Kurrajong NSW 2758</div>
      <div><svg viewBox="0 0 10 10"><rect x="2.2" y=".6" width="5.6" height="8.8" rx="1" fill="none" stroke="#3a3d44"/><circle cx="5" cy="7.8" r=".6" fill="#3a3d44"/></svg>0400 555 219</div>
      <div><svg viewBox="0 0 10 10"><circle cx="5" cy="5" r="4.3" fill="none" stroke="#3a3d44"/><path d="M.7 5h8.6M5 .7c-2.4 2.4-2.4 6.2 0 8.6M5 .7c2.4 2.4 2.4 6.2 0 8.6" fill="none" stroke="#3a3d44" stroke-width=".8"/></svg>marisol@willowmerecollective.example</div>
    </div>
  </footer>
</div>
</body>
</html>
```